Engineering Land Development Company Needs Flyer Brochure for Prospective Professional Clients

Our company provides land development site design for commercial projects. We have many repeat clients that are familiar with our work. We do not advertise our services other than a website. Most of our referrals are from existing clients. When a new client contacts us and asks for a proposal for a project we would like to have a brochure that shows our strengths, experience, and professionalism. We are selling professional services similar to a lawyer or accountant. We want new clients to feel comfortable hiring a new firm. The brochure would be one page single-side included when we submit proposals for new projects. Check out our website at tovamrk.net for more info. We would like a brochure that mixes grading/excavation construction work on a job site with business professional. We will need to update the brochure so we want it in .doc .psd or some other edit format. The brochure we are using is attached. It is very two-dimensional. We need some depth.

Target Market(s)

Land developers, architects, real estate, professionals, attorneys

Industry/Entity Type

Real Estate Development

Font styles to use
Sans Serif
Other font styles liked:
• calibri

Colors
0355a3
9bcb3c

Requirements
Must have
• company logo, ability to update text and images
Nice to have
• background image(s) with text overlay
Should not have
• cartoons, harsh colors, stock photos of people, lots of boxes

```html
<!DOCTYPE html>
<html lang="en">
<head>
<meta charset="utf-8">
<title>Tovamark Engineering PLLC – Flyer</title>
<link href="https://fonts.googleapis.com/css2?family=Carlito:ital,wght@0,400;0,700;1,400;1,700&display=swap" rel="stylesheet">
<style>
  :root {
    --blue: #0355a3;
    --blue-deep: #0b3a78;
    --green: #9bcb3c;
    --green-deep: #6f9a22;
    --ink: #2e2e2e;
    --ink-soft: #4a4a4a;
    --paper: #ffffff;
    --backdrop: #e8e8e8;
  }
  * { box-sizing: border-box; margin: 0; padding: 0; }
  html, body {
    width: 1200px; height: 960px; overflow: hidden;
    background: var(--backdrop);
    font-family: "Carlito", "Calibri", sans-serif;
    color: var(--ink);
  }
  .flyer {
    position: absolute; left: 260px; top: 39px;
    width: 512px; height: 664px;
    background: var(--paper);
    transform: scale(1.328); transform-origin: top left;
    overflow: hidden;
    box-shadow: 0 2px 6px rgba(0,0,0,.15);
  }
  .flyer-shapes { position: absolute; inset: 0; }
  .abs { position: absolute; }

  .brand { left: 7px; top: 28px; display: flex; align-items: center; gap: 8px; }
  .brand-square { width: 24px; height: 24px; background: var(--blue); }
  .brand-name { font-size: 19px; color: var(--blue); font-weight: 400; letter-spacing: -.2px; }
  .contact { left: 39px; top: 58px; font-size: 6.3px; line-height: 8.3px; color: var(--ink); font-style: normal; }

  .slogan {
    right: 8px; top: 40px; text-align: right;
    color: #fff; font-style: italic; font-weight: 700;
    font-size: 13.5px; line-height: 27px;
    text-shadow: 0 1px 2px rgba(0,0,0,.35);
  }
  .intro {
    left: 8px; top: 160px;
    color: #fff; font-style: italic; font-weight: 700;
    font-size: 7.6px; line-height: 18.6px;
  }
  .intro span { display: block; white-space: nowrap; }

  .service { position: absolute; }
  .service-title {
    font-size: 7.6px; font-weight: 700; letter-spacing: .2px;
    padding-bottom: 1px; border-bottom: 1.2px solid var(--green);
    color: var(--ink);
  }
  .service-lead { font-size: 5.7px; font-weight: 700; line-height: 6.2px; margin-top: 3px; padding-left: 6px; }
  .service-body { font-size: 5.3px; line-height: 6px; color: var(--ink-soft); padding-left: 6px; }
  .planning    { left: 280px; top: 232px; width: 224px; }
  .surveying   { left: 224px; top: 309px; width: 232px; }
  .engineering { left: 156px; top: 386px; width: 232px; }
  .environment { left: 80px;  top: 462px; width: 228px; }

  .clients { position: absolute; inset: 0; pointer-events: none; }
  .client {
    position: absolute; font-size: 6.4px; font-weight: 700;
    color: var(--ink); white-space: nowrap;
    transform: translateX(-50%);
  }
  .partner-badge { position: absolute; left: 477px; top: 404px; width: 16px; height: 22px; background: #6b4a2b; border-radius: 3px; }
  .clients-note {
    position: absolute; left: 130px; top: 653px; width: 362px;
    font-size: 6.2px; color: var(--ink); text-align: center; white-space: nowrap;
  }
</style>
</head>
<body>
  <main class="flyer">
    <svg class="flyer-shapes" viewBox="0 0 512 664" width="512" height="664">
      <defs>
        <linearGradient id="siteTone" x1="0" y1="0" x2="0.4" y2="1">
          <stop offset="0" stop-color="#3f8a3c"/>
          <stop offset=".55" stop-color="#6f7b2a"/>
          <stop offset="1" stop-color="#7a5a2e"/>
        </linearGradient>
        <linearGradient id="steelTone" x1="0.5" y1="0" x2="0.2" y2="1">
          <stop offset="0" stop-color="#0a5eae"/>
          <stop offset=".6" stop-color="#0355a3"/>
          <stop offset="1" stop-color="#0b2f5e"/>
        </linearGradient>
        <linearGradient id="thumbTone" x1="0" y1="0" x2="1" y2="1">
          <stop offset="0" stop-color="#c9c3b4"/>
          <stop offset="1" stop-color="#8d8878"/>
        </linearGradient>
        <linearGradient id="leafTone" x1="0" y1="0" x2="1" y2="1">
          <stop offset="0" stop-color="#8fae6a"/>
          <stop offset="1" stop-color="#3f5e2d"/>
        </linearGradient>
      </defs>

      <path role="img" aria-label="Excavator grading soil on a job site"
            d="M312,0 H512 V150 C450,152 390,162 334,178 C306,120 300,55 312,0 Z" fill="url(#siteTone)"/>
      <path d="M296,0 H316 C302,58 310,122 336,178 C304,135 290,62 296,0 Z" fill="var(--green)"/>
      <path d="M334,178 C390,162 450,152 512,150" fill="none" stroke="var(--green)" stroke-width="2"/>

      <path role="img" aria-label="Steel building frame in blue tint behind the introduction text"
            d="M0,88 C120,94 240,120 326,176 C282,285 168,405 0,480 Z" fill="url(#steelTone)"/>

      <path d="M0,628 C220,612 420,470 512,302 L512,318 C432,500 250,650 0,664 Z" fill="var(--green)"/>

      <g stroke="var(--green)" stroke-width="2" fill="#fff">
        <circle cx="241" cy="260" r="33"/>
        <circle cx="185" cy="340" r="33"/>
        <circle cx="118" cy="410" r="33"/>
        <circle cx="42"  cy="469" r="33"/>
      </g>
      <circle role="img" aria-label="Site plan drawings and building model" cx="241" cy="260" r="30" fill="url(#thumbTone)"/>
      <circle role="img" aria-label="Surveyor's instrument on a tripod" cx="185" cy="340" r="30" fill="#9aa07f"/>
      <circle role="img" aria-label="Engineering site plan drawing" cx="118" cy="410" r="30" fill="#d9d9d6"/>
      <circle role="img" aria-label="Green leaves" cx="42" cy="469" r="30" fill="url(#leafTone)"/>
    </svg>

    <header class="brand abs">
      <span class="brand-square"></span>
      <span class="brand-name">Tovamark Engineering PLLC</span>
    </header>
    <address class="contact abs">
      418 Elm Avenue – Suite 300, Linden Falls, NC 28000<br>
      (336) 555-0142<br>
      www.tovamrk.net
    </address>

    <h1 class="slogan abs">Providing<br>superior quality<br>professional land<br>development services.</h1>

    <p class="intro abs">
      <span>Our firm provides</span>
      <span>planning, surveying,</span>
      <span>engineering, and</span>
      <span>environmental services which allows us</span>
      <span>to focus on the entire land development</span>
      <span>process rather than one specific discipline.</span>
      <span>Providing a broad scope of professional</span>
      <span>services helps to streamline a project by</span>
      <span>eliminating many disadvantages of</span>
      <span>having multiple firms with</span>
      <span>overlapping responsibilities.</span>
    </p>

    <section class="service planning">
      <h2 class="service-title">PLANNING</h2>
      <p class="service-lead">We are land development professionals who can see the<br>“big picture”.</p>
      <p class="service-body">We have extensive experience with site selection, due diligence investigations, re-zonings, and land planning. Every project is different. We look forward to identifying all feasible alternatives. We become part of the project and enjoy developing the best plan for the success of each particular project.</p>
    </section>

    <section class="service surveying">
      <h2 class="service-title">SURVEYING</h2>
      <p class="service-lead">We are land development professionals who provide superior quality surveying services.</p>
      <p class="service-body">Our firm can handle any surveying need. We have extensive experience with ALTA surveys, boundary surveys, subdivision platting, topographic/location surveys, GPS surveys, R/W surveys, construction staking, as-built surveys, elevation certificates, etc. We work closely with title attorneys to provide legal descriptions, exhibits, and other assistance when closing the real estate deal.</p>
    </section>

    <section class="service engineering">
      <h2 class="service-title">ENGINEERING</h2>
      <p class="service-lead">We are land development professionals who can handle the most complicated engineering challenge.</p>
      <p class="service-body">Let us worry about all the technical stuff and the regulators. Our firm has extensive experience with infrastructure assessments, erosion control, grading, roadway design, stormwater management, water systems, sewer systems, utilities, flood plain management, landscape design, permitting, bidding, and construction</p>
    </section>

    <section class="service environment">
      <h2 class="service-title">ENVIRONMENT</h2>
      <p class="service-lead">We are land development professionals who provide superior quality environmental services.</p>
      <p class="service-body">We provide environmental site assessments, underground storage tank management, soil and groundwater sampling and testing, contamination remediation, Brownfields assessments, permitting and redevelopment, and wetlands permitting. Our firm works closely with state and federal agencies to provide economical mitigation and remediation solutions.</p>
    </section>

    <div class="clients" aria-label="Project clients">
      <span class="partner-badge"></span>
      <span class="client" style="left:436px;top:463px">Verdeo Grill</span>
      <span class="client" style="left:484px;top:463px">Casa Campana</span>
      <span class="client" style="left:400px;top:506px">Craft Loft</span>
      <span class="client" style="left:452px;top:506px">Griddle House</span>
      <span class="client" style="left:405px;top:550px">Mesa Joe's</span>
      <span class="client" style="left:446px;top:550px">Pie Shack</span>
      <span class="client" style="left:486px;top:550px">Forward Auto</span>
      <span class="client" style="left:282px;top:590px">Field Line</span>
      <span class="client" style="left:325px;top:590px">Tallow Farms</span>
      <span class="client" style="left:372px;top:590px">Larkin Home</span>
      <span class="client" style="left:425px;top:590px">Kaido Motors</span>
      <span class="client" style="left:478px;top:590px">Harbor Roast</span>
      <span class="client" style="left:195px;top:632px">Linkwell</span>
      <span class="client" style="left:250px;top:632px">Pantry Crest</span>
      <span class="client" style="left:302px;top:632px">Bayou Biscuit</span>
      <span class="client" style="left:352px;top:632px">Paws Co</span>
      <span class="client" style="left:404px;top:632px">Chile Verde</span>
      <span class="client" style="left:455px;top:632px">Wing Yard</span>
    </div>
    <p class="clients-note">Our business would not be successful without the support of our clients. Some of our project clients include:</p>
  </main>
</body>
</html>
```